3 in 1 website - Home Lens Studio Extra + Keeping Moments LLC + Marla's Game Shots

Help me simplify and organize my business life. I am a sports photographer (action, individual and teams), real estate photographer (stills and drones) and I transfer videos and photos to jump drives, along with photo restoration, etc. Currently, I have a functioning website for the transfer/restoration business at KeepingMomentsLLC.example which was recently created and I like it. I have received several really good ideas for the Real Estate Photography portion! I don't have anything started for the Sports Pics. My vision possibly includes a main/home page giving people the option to choose real estate, sports or transfer/restoration. I just want them combined into one site....somehow to better organize my businesses and give me ONE place to keep to updated and check for communication. I just updated the brief again and added logo files for my "parent" company called "Keeping Moments". I prefer this logo at the top of the main/home page, please. I previously uploaded the logo for Home Lens Studio Extra which would be used with the real estate portion of my business. At this point, I don't have a logo for the sports photography portion.

Target Market(s)

Real Estate Agents and Brokers; Sports team, parents and boosters; Community members typically 40+ years old

Industry/Entity Type

Real Estate Photography; Local sports teams; Community members 40+ years old

Coding

Coded - Design and coding required

Number of Pages Required

3 page

Requirements
Must have
• At least one page for each area: real estate, sports, digital transfers. The real estate will need to connect to an account I have with QNL for checkout options. The sports page(s) will need to connect to a 3rd party service, also. The digital transfers, photo restorations, etc. would just need a way for them to request service.
Nice to have
• I currently have a website at KeepingMomentsLLC.example for the digital transfer/photo restoration part of my business. I like this website but want it integrated with one main site for all 3 businesses.

```html
<!DOCTYPE html>
<html lang="en">
<head>
<meta charset="utf-8">
<title>Keeping Moments — Preserving Photos and Videos</title>
<link rel="stylesheet" href="https://fonts.googleapis.com/css2?family=Lexend:wght@300;400;500&family=Great+Vibes&display=swap">
<style>
:root{
  --teal:#0f7c8b;
  --orange:#f2461a;
  --ink:#6f6f6f;
  --ink-soft:#8a8a8a;
  --field:#eeeeee;
  --line:#d6d6d6;
  --white:#ffffff;
}
*{box-sizing:border-box;margin:0;padding:0}
html,body{width:1200px;height:2921px;overflow:hidden;background:var(--white)}
body{font-family:"Lexend",sans-serif;font-weight:300;color:var(--ink);position:relative}
.abs{position:absolute}

/* hero */
.hero{position:absolute;left:0;top:0;width:1200px;height:645px;
  background:linear-gradient(180deg,#8fa0a6 0%,#a79a80 18%,#6f6a5e 45%,#4f4a42 75%,#3c3a36 100%)}
.hero-shade{position:absolute;inset:0;background:linear-gradient(90deg,rgba(30,30,30,.35),rgba(30,30,30,0) 60%)}
.menu-icon{left:112px;top:22px}
.brand{left:0;width:1200px;top:22px;text-align:center;color:var(--white)}
.brand-name{font-size:26px;font-weight:300;letter-spacing:1px}
.brand-tag{font-size:8px;letter-spacing:4px;font-weight:400;margin-top:2px}
.social-dot{left:1027px;top:19px;width:24px;height:24px;border-radius:50%;background:var(--white)}
.search-icon{left:1064px;top:19px}
.hero-script{left:113px;top:445px;font-family:"Great Vibes",cursive;font-size:64px;color:var(--white);line-height:1}
.hero-title{left:111px;top:527px;font-size:50px;font-weight:400;color:var(--white);letter-spacing:1px;line-height:1}

/* booking card */
.book-card{left:762px;top:145px;width:325px;height:441px;background:var(--white);padding:28px 0 0 42px}
.book-title{font-size:33px;font-weight:500;color:var(--teal);line-height:38px;letter-spacing:.5px}
.book-sub{font-size:12px;color:var(--ink);margin:8px 0 13px;letter-spacing:.6px}
.field{background:var(--field);height:25px;font-size:10px;color:var(--ink-soft);padding:7px 12px;margin-bottom:8px;width:240px;letter-spacing:.4px}
.field-row{display:flex;gap:6px;width:240px}
.field-row .field{width:117px}
.field.message{height:105px}
.btn{display:block;background:var(--orange);color:var(--white);font-weight:500;text-align:center;letter-spacing:.5px}
.book-btn{width:240px;height:27px;line-height:27px;font-size:9px}

/* intro */
.eyebrow{font-size:12px;color:var(--orange);letter-spacing:.6px;font-weight:400}
.intro-eyebrow{left:111px;top:705px}
.intro-title{left:111px;top:718px;font-size:32px;font-weight:400;color:var(--teal);letter-spacing:.4px}
.intro-copy{left:111px;top:771px;width:505px;font-size:13px;line-height:19px;letter-spacing:.5px}
.intro-copy p+p{margin-top:18px}
.intro-photo{left:681px;top:718px;width:406px;height:241px;background:linear-gradient(180deg,#b9c0c4 0%,#9aa3a2 40%,#66735e 75%,#7d7f78 100%)}

/* skyline */
.skyline{left:0;top:1021px;width:1200px;height:211px;background:linear-gradient(180deg,#4e6a86 0%,#c9a27b 40%,#3f4f66 65%,#5b7fa2 100%)}
.chev{top:1112px}

/* services */
.svc-eyebrow{left:0;width:1200px;top:1260px;text-align:center}
.svc-title{left:0;width:1200px;top:1272px;text-align:center;font-size:32px;font-weight:400;color:var(--teal);letter-spacing:.4px}
.svc-card{top:1326px;width:202px;height:230px;border:1px solid var(--line);text-align:center;padding:14px 18px 0}
.svc-card svg{display:block;margin:0 auto}
.svc-name{font-size:12px;color:var(--teal);letter-spacing:.6px;line-height:15px;margin-top:10px;font-weight:400}
.svc-text{font-size:10px;line-height:12.5px;color:var(--ink);margin-top:12px;letter-spacing:.3px}

/* feature bands */
.band{left:0;width:1200px;height:348px}
.band-scan{top:1586px;background:linear-gradient(90deg,#c7b9a0 0%,#d6a566 35%,#c9c6b6 60%,#b8bbb4 100%)}
.band-conv{top:1934px;background:linear-gradient(90deg,#a9bcc8 0%,#b7c6cf 45%,#3d6075 70%,#5c7c52 100%)}
.band-org{top:2282px;height:347px;background:linear-gradient(90deg,#5a4a3e 0%,#2a2420 35%,#7a6652 60%,#a78a6a 100%)}
.band-copy{position:absolute;width:375px;color:var(--white)}
.band-title{font-size:32px;font-weight:400;letter-spacing:.5px}
.band-text{font-size:12.5px;line-height:15.7px;letter-spacing:.6px;margin-top:17px}
.band-btn{width:143px;height:38px;line-height:38px;font-size:12px;margin-top:19px}

/* footer */
.foot-links{top:2702px;font-size:12.5px;line-height:25px;letter-spacing:1px;color:var(--ink);list-style:none}
.foot-left{left:214px}
.foot-right{left:863px}
.foot-brand{left:0;width:1200px;top:2660px;text-align:center;color:var(--teal)}
.foot-brand .brand-name{font-size:24px}
.foot-brand .brand-tag{font-size:7px;color:var(--teal)}
.foot-info{left:0;width:1200px;top:2717px;text-align:center;font-size:12.5px;line-height:25px;letter-spacing:1px}
.foot-info a{color:var(--teal);text-decoration:none}
.foot-rule{left:0;top:2869px;width:1200px;height:1px;background:var(--line)}
.copyright{left:0;width:1200px;top:2890px;text-align:center;font-size:9px;letter-spacing:.5px;color:var(--ink-soft)}
</style>
</head>
<body>

<header class="hero" role="img" aria-label="Aerial photo of a city skyline at sunset with skyscrapers">
  <div class="hero-shade"></div>
</header>

<svg class="abs menu-icon" width="30" height="22" viewBox="0 0 30 22" aria-hidden="true">
  <g stroke="#fff" stroke-width="2"><line x1="0" y1="2" x2="30" y2="2"/><line x1="0" y1="11" x2="30" y2="11"/><line x1="0" y1="20" x2="30" y2="20"/></g>
</svg>
<div class="abs brand">
  <div class="brand-name">Keeping Moments</div>
  <div class="brand-tag">PRESERVING PHOTOS AND VIDEOS</div>
</div>
<span class="abs social-dot" aria-label="Social page"></span>
<svg class="abs search-icon" width="24" height="24" viewBox="0 0 24 24" aria-label="Search">
  <circle cx="10" cy="10" r="8" fill="none" stroke="#fff" stroke-width="2"/><line x1="16" y1="16" x2="23" y2="23" stroke="#fff" stroke-width="2"/>
</svg>

<div class="abs hero-script">Enjoy all your family</div>
<h1 class="abs hero-title">MEMORIES AGAIN</h1>

<form class="abs book-card">
  <h2 class="book-title">SHOWCASE<br>YOUR LISTING</h2>
  <p class="book-sub">Contact us to book !</p>
  <div class="field-row"><div class="field">Name</div><div class="field">Email</div></div>
  <div class="field">Date</div>
  <div class="field">Phone</div>
  <div class="field">Address</div>
  <div class="field message">Message</div>
  <span class="btn book-btn">GET IN TOUCH</span>
</form>

<section>
  <p class="abs eyebrow intro-eyebrow">NO PROJECT IS IMPOSSIBLE</p>
  <h2 class="abs intro-title">Save, Organize, &amp; Share Photos</h2>
  <div class="abs intro-copy">
    <p>We are a small business and we care for your photos and memories as if they were our own. Over the years, I inherited box and boxes of old family photos, reels, slides and VHS tapes and really didn't know what all I had in the collection. Time, training and research has taught me how to properly care for all of these precious family memories.</p>
    <p>I am an active member of the international organization, The Picture Keepers Guild, and love helping individuals and families go from being overwhelmed with their often, unorganized collection of family pictures, movies and memorabilia to enjoying all of the old family memories.</p>
  </div>
  <div class="abs intro-photo" role="img" aria-label="Video still of a leafy city district seen from above under a cloudy sky"></div>
</section>

<div class="abs skyline" role="img" aria-label="Slideshow photo of a city waterfront skyline and suspension bridge at dusk"></div>
<svg class="abs chev" style="left:110px" width="16" height="28" viewBox="0 0 16 28" aria-label="Previous slide"><polyline points="14,2 2,14 14,26" fill="none" stroke="#fff" stroke-width="2"/></svg>
<svg class="abs chev" style="left:1074px" width="16" height="28" viewBox="0 0 16 28" aria-label="Next slide"><polyline points="2,2 14,14 2,26" fill="none" stroke="#fff" stroke-width="2"/></svg>

<section>
  <p class="abs eyebrow svc-eyebrow">OUR</p>
  <h2 class="abs svc-title">Service</h2>

  <article class="abs svc-card" style="left:279px">
    <svg width="60" height="56" viewBox="0 0 60 56" aria-hidden="true">
      <g fill="none" stroke="var(--orange)" stroke-width="2">
        <circle cx="22" cy="34" r="17"/><path d="M5 34h34M22 17v34M10 22c8 6 16 6 24 0M10 46c8-6 16-6 24 0"/>
        <ellipse cx="46" cy="14" rx="10" ry="12"/><line x1="40" y1="24" x2="32" y2="40"/>
      </g>
    </svg>
    <h3 class="svc-name">SPORTS<br>PHOTOGRAPHER</h3>
    <p class="svc-text">Lorem ipsum dolor sit amet, consectetur adipiscing elit, sed do eiusmod tempor incididunt ut labore et dolore magna aliqua. Quis ipsum suspendisse ultrices gravida. Risus commodo viverra</p>
  </article>

  <article class="abs svc-card" style="left:499px">
    <svg width="60" height="56" viewBox="0 0 60 56" aria-hidden="true">
      <g fill="none" stroke="var(--orange)" stroke-width="2">
        <path d="M14 4h24l8 8v40H14z"/><path d="M20 28l10-9 10 9M23 26v10h14V26"/><line x1="52" y1="30" x2="38" y2="50"/>
      </g>
    </svg>
    <h3 class="svc-name">REAL ESTATE<br>PHOTOGRAPHER</h3>
    <p class="svc-text">Lorem ipsum dolor sit amet, consectetur adipiscing elit, sed do eiusmod tempor incididunt ut labore et dolore magna aliqua. Quis ipsum suspendisse ultrices gravida. Risus commodo viverra</p>
  </article>

  <article class="abs svc-card" style="left:719px">
    <svg width="60" height="56" viewBox="0 0 60 56" aria-hidden="true">
      <g fill="none" stroke="var(--orange)" stroke-width="2">
        <rect x="8" y="18" width="44" height="30" rx="4"/><path d="M22 18l3-6h10l3 6"/><circle cx="32" cy="33" r="9"/><circle cx="32" cy="33" r="4"/><line x1="13" y1="24" x2="18" y2="24"/>
      </g>
    </svg>
    <h3 class="svc-name">PHOTO<br>RESTORATION</h3>
    <p class="svc-text">Lorem ipsum dolor sit amet, consectetur adipiscing elit, sed do eiusmod tempor incididunt ut labore et dolore magna aliqua. Quis ipsum suspendisse ultrices gravida. Risus commodo viverra</p>
  </article>
</section>

<section class="abs band band-scan" role="img" aria-label="Photo of a runner's shoe mid-stride on a sunlit bridge">
  <div class="band-copy" style="left:690px;top:78px">
    <h2 class="band-title">Scanning</h2>
    <p class="band-text">Do you have boxes and boxes of old photos and/or documents you haven't looked at in years? Do you have old photos that need to be restored? Let us scan your photos so they are preserved and easily accessible to enjoy now and for future generations.</p>
    <span class="btn band-btn">LEARN MORE</span>
  </div>
</section>

<section class="abs band band-conv" role="img" aria-label="Photo of glass office towers beside green trees under a pale sky">
  <div class="band-copy" style="left:112px;top:77px">
    <h2 class="band-title">Conversions</h2>
    <p class="band-text">Do you have old family videos on VHS, Beta, 8 mm, or Super 8 mm, but no way to enjoy them again? Let us convert them to a digital format. Enjoy old family videos and special events that haven't been watched in decades.</p>
    <span class="btn band-btn">LEARN MORE</span>
  </div>
</section>

<section class="abs band band-org" role="img" aria-label="Photo of a hand holding a coffee cup over a scattered pile of printed photographs">
  <div class="band-copy" style="left:690px;top:76px">
    <h2 class="band-title">Photo Organizing</h2>
    <p class="band-text">Overwhelmed with boxes and boxes of photos? Let us help you organize your printed and digital photos so you can enjoy your precious family photos again. We will meet and talk about YOUR goals for YOUR photos, then we will plan on how to proceed.</p>
    <span class="btn band-btn">LEARN MORE</span>
  </div>
</section>

<footer>
  <ul class="abs foot-links foot-left">
    <li>Home</li><li>Services</li><li>Contact Us</li><li>Projects</li><li>Aerial</li><li>Blog</li>
  </ul>
  <div class="abs foot-brand">
    <div class="brand-name">Keeping Moments</div>
    <div class="brand-tag">PRESERVING PHOTOS AND VIDEOS</div>
  </div>
  <address class="abs foot-info" style="font-style:normal">
    Dana Whitfield<br>
    Keeping Moments LLC<br>
    2480 Orchard Lane<br>
    Maple Falls, KY 40012<br>
    <a href="mailto:hello@keepingmoments.example">hello@keepingmoments.example</a>
  </address>
  <ul class="abs foot-links foot-right">
    <li>About Me</li><li>Services Offered</li><li>Client Reviews</li><li>Request A Meeting</li>
  </ul>
  <div class="abs foot-rule"></div>
  <p class="abs copyright">© 2023 COPYRIGHT KEEPING MOMENTS. ALL RIGHTS RESERVED.</p>
</footer>

</body>
</html>
```